Stationery Design Project - Mark Delouris

I have recently designed my personal logo - Mark Delouris (here on briefhivo.net) and now i'm looking to complete my corporate identity, with adding:
- Business Card
- Letter Head
- Envelope
- Brochure template (that will be used to promote any of the workshops or other services I provide along with a short summary about my credentials, and testimonials) - you can take your pick from the website: http://markdelouris.net

Refer to website for more insight into the brand and the look & feel

PS.
- PLEASE REFER TO ATTACHED FILE AND READ THE "SHOULD NOT HAVE SECTION OF THIS BRIEF"
- I have attached two vector files, displaying the logo alteration on two different backgrounds (dark & light)

ONLY 2 DAYS LEFT ON DEADLINE. KEEP THOSE DESIGNS COMING.

Target Market(s)

1) One-on-one Business Executive 2) Companies requesting my workshops for mid management teams & public speaking events like KIP Forums

Industry/Entity Type

Business

Requirements
Must have
• - must fit the look and feel of the logo (notice that I have attached the logo, and an emblem)
- the final files should be ready for printing - with info on colours, sizes, bleed area, margins, UV spot (if applicable), suggested material to print on (applies to business cards in particular)
- brand guide lines should be laid out too (font, colour, etc ...)
Nice to have
• It would be nice to produce something different that your standard sizes & di-cut in terms of business card, and letter head ...
Should not have
• THE EMBLEM (MD) AND THE LOGO (MARK DELOURIS) SHOULD NOT BE LAYED OUT AS PER THE ATTACHED FILE - THEY SHOULD BE SEPARATED - THE EMBLEM (MD) CAN BE USED IN PARTIAL OR AS WATERMARK - BUT NOT THE LOGO (MARK DELOURIS)

```html
<!DOCTYPE html>
<html lang="en">
<head>
<meta charset="utf-8">
<title>Mark Delouris – Stationery</title>
<link rel="stylesheet" href="https://fonts.googleapis.com/css2?family=Questrial&display=swap">
<style>
  :root {
    --backdrop: #e6e6e6;
    --paper: #ffffff;
    --brand-blue: #4dc1ee;
    --brand-grey: #555759;
    --bar-dark-a: #4a4a4a;
    --bar-dark-b: #7a7a7a;
    --ink: #1c1c1c;
  }
  * { box-sizing: border-box; margin: 0; padding: 0; }
  html, body {
    width: 1186px; height: 1200px; overflow: hidden;
    background: var(--backdrop);
    font-family: "Questrial", "Century Gothic", sans-serif;
    color: var(--ink);
  }
  .letterhead {
    position: absolute; left: 171px; top: 37px;
    width: 843px; height: 1102px;
    background: var(--paper);
  }
  .stripe { position: absolute; display: flex; gap: 3px; }
  .stripe span { display: block; height: 100%; }
  .stripe .dark { background: linear-gradient(90deg, var(--bar-dark-a), var(--bar-dark-b)); }
  .stripe .blue { background: var(--brand-blue); }
  .letterhead-stripe { left: 0; top: 41px; width: 843px; height: 7px; }
  .letterhead-stripe .short { flex: 87; }
  .letterhead-stripe .long { flex: 231; }

  .wordmark { position: absolute; text-align: center; }
  .wordmark .emblem-circle { display: block; margin: 0 auto; border-radius: 50%; }
  .wordmark .name { display: block; letter-spacing: 0.3px; white-space: nowrap; }

  .letterhead-mark { left: 45px; top: 76px; width: 202px; }
  .letterhead-mark .emblem-circle { width: 56px; height: 56px; border: 5px solid var(--brand-grey); }
  .letterhead-mark .name { font-size: 25px; color: var(--brand-grey); margin-top: 8px; line-height: 1.1; }
  .letterhead-mark .rule { display: block; height: 1px; background: var(--brand-blue); margin-top: 5px; }

  .date { position: absolute; right: 58px; top: 126px; font-size: 17.5px; color: var(--ink); }

  .card { position: absolute; width: 345px; overflow: hidden; }
  .card-front { left: 198px; top: 376px; height: 192px; background: var(--paper); border: 1px solid #ececec; }
  .card-front .holder {
    position: absolute; left: 13px; top: 8px; font-size: 18px; color: var(--brand-blue);
    border-bottom: 1px solid var(--brand-blue); padding-bottom: 1px;
  }
  .card-front .phones {
    position: absolute; right: 13px; top: 13px; font-size: 10.5px; line-height: 15px; text-align: right; font-weight: 700;
  }
  .card-front .card-mark { left: 0; right: 0; top: 58px; }
  .card-front .card-mark .emblem-circle { width: 28px; height: 28px; border: 3px solid var(--brand-grey); }
  .card-front .card-mark .name { font-size: 13.5px; color: var(--brand-grey); margin-top: 5px; }
  .card-front .details {
    position: absolute; left: 0; right: 0; top: 134px; text-align: center;
    font-size: 11.5px; line-height: 16px; font-weight: 700;
  }
  .card-front .details .web { word-spacing: 2px; }
  .card-stripe { left: 0; bottom: 14px; width: 345px; height: 3px; }
  .card-stripe .short { flex: 36; }
  .card-stripe .long { flex: 98; }

  .card-back { left: 417px; top: 628px; height: 199px; background: var(--brand-blue); }
  .card-back .card-mark { left: 0; right: 0; top: 54px; }
  .card-back .card-mark .emblem-circle { width: 42px; height: 42px; border: 4px solid var(--paper); }
  .card-back .card-mark .name { font-size: 20px; color: var(--paper); margin-top: 10px; }

  .sender { position: absolute; left: 60px; top: 906px; font-weight: 700; font-style: normal; }
  .sender .sender-name { font-size: 21px; color: var(--brand-blue); font-weight: 400; margin-bottom: 2px; }
  .sender .line { font-size: 14.5px; line-height: 20px; }

  .footer-stripe { left: 611px; top: 1046px; width: 180px; height: 5px; }
  .footer-stripe span { flex: 1; }
</style>
</head>
<body>
  <main class="letterhead">
    <div class="stripe letterhead-stripe">
      <span class="dark short"></span><span class="dark short"></span>
      <span class="blue long"></span><span class="blue long"></span>
      <span class="dark short"></span><span class="dark short"></span>
    </div>

    <div class="wordmark letterhead-mark">
      <span class="emblem-circle"></span>
      <span class="name">MARK DELOURIS</span>
      <span class="rule"></span>
    </div>

    <p class="date">16 October 2012</p>

    <section class="card card-front">
      <p class="holder">Mark Delouris</p>
      <p class="phones">+31 (6) 55 01 23 45<br>+31 (6) 55 01 23 45</p>
      <div class="wordmark card-mark">
        <span class="emblem-circle"></span>
        <span class="name">MARK DELOURIS</span>
      </div>
      <div class="details">
        <p>Street, Region, Country&nbsp; PO BOX 321</p>
        <p class="web">www.markdelouris.net&nbsp; info@markdelouris.net</p>
      </div>
      <div class="stripe card-stripe">
        <span class="blue short"></span><span class="blue short"></span>
        <span class="dark long"></span><span class="dark long"></span>
        <span class="blue short"></span><span class="blue short"></span>
      </div>
    </section>

    <section class="card card-back">
      <div class="wordmark card-mark">
        <span class="emblem-circle"></span>
        <span class="name">MARK DELOURIS</span>
      </div>
    </section>

    <address class="sender">
      <p class="sender-name">Mark Delouris</p>
      <p class="line">Street, Region, Country</p>
      <p class="line">PO BOX 321</p>
      <p class="line">+31 (6) 55 01 23 45</p>
      <p class="line">+31 (6) 55 09 87 65</p>
      <p class="line">info@markdelouris.net</p>
      <p class="line">www.markdelouris.net</p>
    </address>

    <div class="stripe footer-stripe">
      <span class="dark"></span><span class="blue"></span>
    </div>
  </main>
</body>
</html>
```